WordPress Website for Pain Relief Clinic

I need a WordPress website designed for my laser pain relief clinic. It needs to be a professional, responsive design with 7 pages: Home, Why Choose Us, Treatable Conditions, Testimonials, FAQ, Franchising, Contact Us. Here is logo: https://s3.cloudvexa-store.net/media.b-r-t-n.net/sitebuilder/361/KelvaroLogoHighQuality.png

Target Market(s)

people with pain,elderly adults,injuries,soreness

Industry/Entity Type

Clinic

Number of Pages Required

5+ page

Colors
0792cd
85abd2

```html
<!DOCTYPE html>
<html lang="en">
<head>
<meta charset="utf-8">
<title>Kelvaro Laser Pain Relief</title>
<link rel="stylesheet" href="https://fonts.googleapis.com/css2?family=Montserrat:wght@400;600;700&family=Lato:ital,wght@0,400;0,700;1,400&display=swap">
<style>
:root{
  --blue:#2b80d6;
  --brand:#0792cd;
  --dark:#2b3038;
  --white:#ffffff;
  --ink:#3a3d42;
  --muted:#8f9399;
  --leaf:#3fb38f;
  --mint:#5fc6a0;
  --foot:#f0f0f0;
}
*{box-sizing:border-box;margin:0;padding:0}
html,body{width:1200px;height:3216px;overflow:hidden}
body{position:relative;background:var(--white);font-family:'Lato',sans-serif;color:var(--ink)}
.abs{position:absolute}
.nav{left:0;top:0;width:1200px;height:104px;background:var(--white);display:flex;align-items:center;justify-content:center;gap:0}
.nav a{font-family:'Montserrat',sans-serif;font-size:15px;font-weight:600;letter-spacing:2px;color:var(--ink);text-decoration:none;position:absolute;top:44px}
.brand{position:absolute;left:600px;top:22px;transform:translateX(-50%);font-family:'Montserrat',sans-serif;font-weight:700;font-size:44px;color:var(--brand);letter-spacing:-1px}
.hero{left:0;top:104px;width:1200px;height:496px;background:linear-gradient(180deg,#c8c8c8,#9a9a9a 60%,#8a8a8a)}
.hero h1{position:absolute;left:0;width:1200px;top:214px;text-align:center;font-family:'Montserrat',sans-serif;font-weight:600;font-size:38px;line-height:48px;letter-spacing:3px;color:var(--white)}
.band{left:0;top:600px;width:1200px;height:352px;background:var(--blue);text-align:center;color:var(--white)}
.band h2{position:absolute;left:0;width:1200px;top:128px;font-family:'Montserrat',sans-serif;font-weight:700;font-size:20px;letter-spacing:3px}
.band p{position:absolute;left:300px;width:600px;top:168px;font-size:13px;line-height:22px;opacity:.92}
.leaf{position:absolute}
.photo{position:absolute}
.panel{position:absolute;background:var(--white);text-align:center}
.panel h3{font-family:'Montserrat',sans-serif;font-weight:700;font-size:16px;letter-spacing:3px;color:var(--ink);margin-top:78px}
.panel p{font-size:13px;line-height:21px;color:var(--muted);margin:18px auto 0;width:320px}
.review{left:0;top:2300px;width:1200px;height:380px;background:var(--blue);text-align:center;color:var(--white)}
.review h2{position:absolute;left:0;width:1200px;top:94px;font-family:'Lato',sans-serif;font-weight:700;font-size:34px;letter-spacing:1px}
.review p{position:absolute;left:230px;width:740px;top:166px;font-style:italic;font-size:19px;line-height:32px}
.dots{position:absolute;left:582px;top:292px;display:flex;gap:8px}
.dots span{width:8px;height:8px;border-radius:50%;background:rgba(255,255,255,.45)}
.dots span:first-child{background:var(--white)}
.cta{left:0;top:2680px;width:1200px;height:348px;background:var(--dark);text-align:center}
.cta h2{position:absolute;left:0;width:1200px;top:114px;font-family:'Lato',sans-serif;font-weight:400;font-size:18px;color:var(--white)}
.field{position:absolute;left:400px;top:158px;width:300px;height:50px;background:var(--white);font-size:12px;color:#b0b3b8;text-align:left;padding:17px 18px}
.submit{position:absolute;left:712px;top:158px;width:100px;height:50px;background:var(--mint);color:var(--white);font-size:13px;font-weight:700;padding-top:16px}
.footer{left:0;top:3028px;width:1200px;height:188px;background:var(--foot)}
.address{position:absolute;left:186px;top:64px;font-size:12px;line-height:17px;color:var(--muted)}
.social{position:absolute;left:552px;top:74px;display:flex;gap:14px}
.social span{width:24px;height:24px;border-radius:50%}
.copy{position:absolute;left:900px;top:82px;font-size:12px;color:var(--muted)}
</style>
</head>
<body>

<header class="abs nav">
  <a style="left:234px">NEWS</a>
  <a style="left:352px">PRODUCTS</a>
  <div class="brand">Kelvaro</div>
  <a style="left:746px">ABOUT US</a>
  <a style="left:900px">CONTACT US</a>
</header>

<section class="abs hero" role="img" aria-label="Photo of a man shouting in pain against a grey wall">
  <h1>GOT UNBERABLE PAIN?<br>COME HERE FOR BEST RELEIF</h1>
</section>

<section class="abs band">
  <svg class="leaf" style="left:584px;top:78px" width="32" height="32" viewBox="0 0 32 32" aria-hidden="true">
    <path d="M6 26 C6 12 14 6 26 6 C26 18 20 26 6 26 Z" fill="var(--leaf)"/>
    <path d="M8 24 L22 10" stroke="var(--blue)" stroke-width="2"/>
  </svg>
  <h2>A NEW GENERATION OF LASER PAIN RELIEF TREATEMENT</h2>
  <p>Lorem Ipsum is simply dummy text of the printing and typesetting industry. Lorem Ipsum has been the industry's standard dummy text ever since the 1500s, when an unknown printer took a galley of type and scrambled it to make a type specimen book. It has survived not only five centuries, but also the leap into electronic typesetting.</p>
</section>

<!-- Row 1 -->
<div class="photo" style="left:0;top:952px;width:800px;height:448px;background:linear-gradient(135deg,#d9c8b6,#b08a6e 55%,#7e5a44)" role="img" aria-label="Therapist applying a laser device to a patient's back"></div>
<div class="panel" style="left:800px;top:952px;width:400px;height:280px">
  <svg class="leaf" style="left:184px;top:40px" width="32" height="28" viewBox="0 0 32 32" aria-hidden="true"><path d="M6 26 C6 12 14 6 26 6 C26 18 20 26 6 26 Z" fill="var(--leaf)"/><path d="M8 24 L22 10" stroke="#fff" stroke-width="2"/></svg>
  <h3>HEADING</h3>
  <p>Lorem Ipsum is simply dummy text of the printing and typesetting industry. Lorem Ipsum has been the industry's standard dummy text ever since the 1500s, when an unknown printer took a galley of type and scrambled it to make a type specimen book.</p>
</div>
<div class="photo" style="left:800px;top:1232px;width:400px;height:168px;background:linear-gradient(90deg,#8fb07a,#c9a68c 50%,#d6b39a)" role="img" aria-label="Laser probe held against a patient's shoulder"></div>

<!-- Row 2 -->
<div class="panel" style="left:0;top:1400px;width:400px;height:240px">
  <svg class="leaf" style="left:184px;top:40px" width="32" height="28" viewBox="0 0 32 32" aria-hidden="true"><path d="M6 26 C6 12 14 6 26 6 C26 18 20 26 6 26 Z" fill="var(--leaf)"/><path d="M8 24 L22 10" stroke="#fff" stroke-width="2"/></svg>
  <h3>LOREM IPSUM</h3>
  <p>Lorem Ipsum is simply dummy text of the printing and typesetting industry. Lorem Ipsum has been the industry's standard dummy text ever since the 1500s, when an unknown printer took a galley of type and scrambled it to make a type specimen book.</p>
</div>
<div class="photo" style="left:0;top:1640px;width:400px;height:212px;background:linear-gradient(180deg,#1a3f8f,#2f6fd0 50%,#0f2a66)" role="img" aria-label="Blue x-ray style image of a human spine"></div>
<div class="photo" style="left:400px;top:1400px;width:800px;height:452px;background:radial-gradient(circle at 52% 38%,#c23a2e 0,#7a3a34 16%,#3a3a3a 40%,#0e0e0e 75%)" role="img" aria-label="Muscular back with a highlighted red pain area on the shoulder"></div>

<!-- Row 3 -->
<div class="photo" style="left:0;top:1852px;width:400px;height:448px;background:linear-gradient(135deg,#c9a27a,#8a6448 60%,#5a4030)" role="img" aria-label="Illustrated knee and joint pain points"></div>
<div class="panel" style="left:400px;top:1852px;width:400px;height:308px">
  <svg class="leaf" style="left:186px;top:40px" width="28" height="30" viewBox="0 0 28 30" aria-hidden="true"><path d="M4 4 L14 18 L24 4 M14 18 L14 28" stroke="var(--leaf)" stroke-width="3" fill="none" stroke-linecap="round"/></svg>
  <h3>TITLE OF CONTENT</h3>
  <p>Lorem Ipsum is simply dummy text of the printing and typesetting industry. Lorem Ipsum has been the industry's standard dummy text ever since the 1500s, when an unknown printer took a galley of type and scrambled it to make a type specimen book.</p>
</div>
<div class="photo" style="left:400px;top:2160px;width:400px;height:140px;background:linear-gradient(90deg,#e8e2dc,#b89a86 50%,#403a44)" role="img" aria-label="Patient lying on a treatment table during therapy"></div>
<div class="photo" style="left:800px;top:1852px;width:400px;height:448px;background:linear-gradient(135deg,#d8d8d8,#7a7a7a 55%,#3a3a3a)" role="img" aria-label="Black and white photo of a hand gripping a sore shoulder"></div>

<section class="abs review">
  <h2>Customers Review</h2>
  <p>Lorem ipsum dolor sit amet, consectetur adipiscing elit. Sed ut tellus ac nulla semper rhoncus. Nullam a odio porttitor, dictum turpis vitae, pretium ante amet.</p>
  <div class="dots"><span></span><span></span><span></span></div>
</section>

<section class="abs cta">
  <h2>Grab our appointment Now!!!</h2>
  <div class="field">Enter your email</div>
  <div class="submit">Submit</div>
</section>

<footer class="abs footer">
  <div class="address">Kelvaro Clinic<br>240 Birchfield Avenue<br>Northvale, NY 10482<br>hello@kelvaro-care.com</div>
  <div class="social">
    <span style="background:#4cb6e6"></span>
    <span style="background:#3b5a9a"></span>
    <span style="background:#d9453a"></span>
  </div>
  <div class="copy">Copyright Kelvaro Clinic</div>
</footer>

</body>
</html>
```